HIgh-end jewelry designer needs a business card design

I need a business card design for the ecclectic & rather expensive jewelry designs. My approach to my work is to combine very old jewelry offset with contemporary items. I enjoy the idea of legacy as well as repurposing finely crafted items that are not possible to create any longer. My desire is to celebrate the past in a contemporary & funky way. The name of my business is MERIVALE. I see my business card design as simple & yet enigmatic as possible. In the end... clean, simple & understated is the look I am after. Thank you for your consideration...

Target Market(s)

I will use this business card for the trade as well as customers

Industry/Entity Type

Business

Contact Information for Business Card

Corinne Halvard Owner/Designer 555-274-8163

Requirements
Must have
• Clean & simple sophisticated design using the word "Merivalle" as the logo. I like the idea of a play on the word itself, perhaps even using different fonts (i.e.: a bold helvetica combined with a lovely script). I'm afraid to say more because I don't want to limit creative input. Gosh, sometimes it's ok to break the rules!
Nice to have
• In my mind, I have imagined this business card to be simple, using my company name "Merivale" in a playful yet sophisticated manner. I believe that doing something beautifully simple can be a true challenge. I have imagined something with just black & white, however I am open to ideas... after all that's why I'm here!
Should not have
• As Mozart once said... "It has too many notes!" I know I'm being silly, but I don't want it to be complicated or overly ornate.

```html
<!DOCTYPE html>
<html lang="en">
<head>
<meta charset="utf-8">
<title>Merivale business card</title>
<link rel="stylesheet" href="https://fonts.googleapis.com/css2?family=Montserrat:wght@300;400&display=swap">
<style>
  :root {
    --backdrop: #2b2b2d;
    --card-dark: #1d181c;
    --card-light: #f4f4f4;
    --ink-silver: #cfcfd1;
    --ink-dark: #3a3a3a;
    --rule: #6a6a6a;
  }
  * { margin: 0; padding: 0; box-sizing: border-box; }
  html, body {
    width: 1200px;
    height: 900px;
    overflow: hidden;
    background: var(--backdrop);
    font-family: "Montserrat", Arial, sans-serif;
  }
  .sheet {
    width: 1200px;
    height: 900px;
    display: flex;
    flex-direction: column;
    align-items: center;
    justify-content: center;
    gap: 60px;
  }
  .card {
    position: relative;
    width: 560px;
    height: 320px;
    border-radius: 26px;
    box-shadow: 0 14px 30px rgba(0,0,0,0.45);
  }
  .card--back {
    background: var(--card-dark);
    display: flex;
    align-items: center;
    justify-content: center;
  }
  .card--front {
    background: var(--card-light);
  }
  .wordmark {
    font-weight: 300;
    letter-spacing: 0.5px;
    line-height: 1;
  }
  .card--back .wordmark {
    color: var(--ink-silver);
    font-size: 40px;
  }
  .card--front .wordmark {
    position: absolute;
    top: 112px;
    left: 0;
    right: 0;
    text-align: center;
    color: var(--ink-dark);
    font-size: 50px;
  }
  .contact-rule {
    position: absolute;
    left: 48px;
    right: 48px;
    top: 226px;
    height: 1px;
    background: var(--rule);
  }
  .contact-line {
    position: absolute;
    left: 48px;
    right: 48px;
    top: 240px;
    display: flex;
    justify-content: space-between;
    font-size: 14px;
    font-weight: 400;
    letter-spacing: 1.2px;
    text-transform: uppercase;
    color: var(--ink-dark);
  }
  .contact-line .person span + span { margin-left: 14px; }
</style>
</head>
<body>
  <main class="sheet">
    <section class="card card--back" aria-label="Card back">
      <div class="wordmark">merivale</div>
    </section>
    <section class="card card--front" aria-label="Card front">
      <div class="wordmark">merivale</div>
      <div class="contact-rule"></div>
      <div class="contact-line">
        <p class="person"><span class="name">Corinne Halvard</span><span class="role">Owner/Designer</span></p>
        <p class="phone">555-274-8163</p>
      </div>
    </section>
  </main>
</body>
</html>
```